Stationary and document suite for consultancy business in Australia called Lumara

I would like to get a suite of documents suitable for my new business called Lumara. I have included the original brief below, however have already selected a design for the logo. I would like to get:
Letter head - simple letter template with "V" logo embossed in background
Word document - standard format with "V" logo embossed in background
Proposal document - bolder pages with cover and back cover, include empty pages with footer as well as contents
Powerpoint presentation - open to ideas
Email signature - banner style or text, open to ideas
Brief that was given for logo (logo not required)
The name of the business is derived from the latin word for green ("Viridis") combined with "co" which is intended to represent a number of different words: collaborative, cooperative, coaching, collective,  construction, consulting, etc.
My objective for the brand is to represent a dynamic, progressive and collaborative business, where our people have fun and enjoy their work.
The objective of our business is to provide consultancy services to construction businesses, mainly aimed at building high performing teams and strategic growth. We will create learning and development tools that businesses can use to increase staff satisfaction and retention. Our future goal is to invest in decarbonisation and sustainability technology for use in the construction industry.
Our target market is construction business leaders and infrastructure owners, who operate road, rail and utility assets. We also want to present as a dynamic, progressive and fun place to work that will be attractive to new employees.

```html
<!DOCTYPE html>
<html lang="en">
<head>
<meta charset="utf-8">
<title>Lumara Stationery Suite</title>
<link rel="stylesheet" href="https://fonts.googleapis.com/css2?family=Open+Sans:ital,wght@0,400;0,600;0,700;1,400&family=Sacramento&display=swap">
<style>
:root{
  --stage:#43a000;
  --leaf:#8dc63f;
  --leaf-dark:#76b02c;
  --ink:#4a4a4a;
  --mark:#5f6062;
  --charcoal:#404043;
  --paper:#ffffff;
  --paper-soft:#f3f3f3;
  --muted:#8a8a8a;
}
*{box-sizing:border-box;margin:0;padding:0}
html,body{width:1200px;height:797px;overflow:hidden}
body{background:var(--stage);font-family:"Open Sans",Arial,sans-serif;color:var(--ink);position:relative}
.sheet{position:absolute;box-shadow:0 6px 18px rgba(0,0,0,.25);overflow:hidden}
.wordmark{font-family:"Open Sans",Arial,sans-serif;font-weight:600;color:var(--mark);letter-spacing:.04em;line-height:1;white-space:nowrap}
.wordmark.light{color:var(--paper)}
.masthead{position:absolute;display:flex;align-items:flex-end;gap:8px}
.masthead .rule{flex:1;height:1px;margin-bottom:4px}
.icon{flex:none}

/* Folder */
.folder{left:40px;top:40px;width:340px;height:481px;background:var(--leaf)}
.folder .masthead{left:28px;right:26px;top:30px}
.folder .wordmark{font-size:26px}
.folder .rule{background:var(--paper)}
.folder .foot{position:absolute;left:28px;bottom:28px;display:flex;align-items:center;gap:8px;color:var(--paper);font-size:12px;letter-spacing:.25em}
.folder .spine{position:absolute;left:0;bottom:0;width:100%;height:8px;background:var(--charcoal)}

/* Letterhead */
.letter{left:400px;top:40px;width:340px;height:481px;background:var(--paper)}
.letter .masthead{left:26px;right:26px;top:28px}
.letter .wordmark{font-size:22px}
.letter .rule{background:var(--leaf)}
.letter .address{position:absolute;left:26px;top:74px;font-size:6.5px;font-weight:600;line-height:1.5}
.letter .body{position:absolute;left:26px;top:124px;width:288px;font-size:6.5px;line-height:1.6;color:#555}
.letter .body p{margin-bottom:6px}
.letter .body .strong{font-weight:600;color:var(--ink)}
.letter .footer{position:absolute;left:26px;top:392px;display:flex;gap:14px;align-items:flex-start}
.letter .footer .wordmark{font-size:16px;margin-top:6px}
.letter .footer .divider{width:1px;height:52px;background:var(--leaf)}
.letter .corner{position:absolute;right:0;bottom:0}

/* Contact block */
.contact .sig{font-family:"Sacramento",cursive;color:var(--ink);line-height:1}
.contact .name{font-weight:600;color:var(--leaf);letter-spacing:.04em;text-transform:uppercase}
.contact .role{color:var(--ink);letter-spacing:.18em}
.contact .line{display:flex;align-items:center;gap:5px;color:var(--ink);letter-spacing:.1em}
.letter .contact .sig{font-size:11px}
.letter .contact .name{font-size:6.5px}
.letter .contact .role{font-size:6.5px}
.letter .contact .line{font-size:5.5px;margin-top:2px}

/* Business cards */
.card{top:40px;width:185px;height:110px}
.card-front{left:770px;background:var(--paper);padding:18px}
.card-front .wordmark{font-size:17px}
.card-front .contact{position:absolute;left:18px;bottom:14px}
.card-front .name{font-size:7px;color:var(--ink)}
.card-front .role{font-size:6px}
.card-front .line{font-size:5.5px;margin-top:2px}
.card-back{left:975px;background:var(--charcoal);display:flex;flex-direction:column;justify-content:space-between;padding:18px}
.card-back .wordmark{font-size:19px}
.card-back .web{display:flex;align-items:center;gap:5px;color:var(--paper);font-size:6px;letter-spacing:.2em;align-self:flex-end}

/* Envelopes */
.envelope{left:770px;width:390px;height:195px;background:var(--paper-soft);display:flex;align-items:center}
.env-photo{top:170px}
.env-plain{top:385px}
.envelope .left{width:195px;display:flex;flex-direction:column;align-items:center;justify-content:center;gap:8px}
.envelope .divider{width:1px;height:96px;background:var(--leaf)}
.envelope .right{padding-left:22px}
.portrait{width:62px;height:62px;border-radius:50%;border:2px solid var(--leaf);background:radial-gradient(circle at 50% 40%,#c9a98e 0 30%,#6b9cc9 60%,#dcdcdc 100%)}
.env-photo .left .name{font-size:10px;color:var(--ink)}
.env-photo .left .role{font-size:9px;color:var(--leaf)}
.envelope .wordmark.big{font-size:34px}
.envelope .contact .sig{font-size:20px;margin-bottom:4px}
.envelope .contact .name{font-size:11px}
.envelope .contact .role{font-size:10px;margin-bottom:6px}
.envelope .contact .line{font-size:8px;margin-top:4px}
.envelope .rule-under{width:140px;height:1px;background:var(--leaf);margin:4px 0 6px}
.envelope .mark-small{font-size:22px;margin:2px 0 4px}

/* Poster banner and gift box lid */
.poster{left:40px;top:600px;width:700px;height:157px;background:var(--paper);display:flex;align-items:center;justify-content:center}
.poster .wordmark{font-size:52px}
.box-lid{left:770px;top:600px;width:390px;height:157px;background:var(--paper-soft);display:flex;align-items:center;justify-content:center;border:6px solid var(--paper)}
.box-lid .wordmark{font-size:38px}
</style>
</head>
<body>

<section class="sheet folder" aria-label="Presentation folder cover">
  <div class="masthead">
    <div class="wordmark light">Lumara</div>
    <div class="rule"></div>
  </div>
  <div class="foot">
    <svg class="icon" width="14" height="14" viewBox="0 0 14 14"><circle cx="7" cy="7" r="6.5" fill="none" stroke="#fff"/><ellipse cx="7" cy="7" rx="3" ry="6.5" fill="none" stroke="#fff"/><line x1="0.5" y1="7" x2="13.5" y2="7" stroke="#fff"/></svg>
    <span>lumara.com.au</span>
  </div>
  <div class="spine"></div>
</section>

<section class="sheet letter" aria-label="Letterhead">
  <div class="masthead">
    <div class="wordmark">Lumara</div>
    <div class="rule"></div>
  </div>
  <div class="address">To,<br>Mr. Alex Reed<br>Chairman<br>Australia</div>
  <div class="body">
    <p>Dear Sir,<br>This is a sample letter that has been placed to demonstrate the typing format on the Lumara letterhead design. When positioned properly, it will serve to work in harmony with all of the other elements on the letterhead.</p>
    <p>This letterhead design is meant to project an image of professionalism and reliability. By using simple alignments we have created a very spacious feeling. The simplicity suggests strength and the spaciousness contributes to the aesthetics of the layout. These basic qualities along with the Lumara colours are consistent with the overall look and help to reinforce the Lumara brand.</p>
    <p class="strong">The simplicity suggests strength and the spaciousness contributes to the aesthetics of the layout. These basic qualities along with the Lumara colours are consistent with the overall look and help to reinforce the Lumara brand and reliability.</p>
    <p>This letterhead design is based on the form of your name. Each stationery piece is part of the same family.</p>
    <p>Sincerely yours,<br><br><strong>Owen Marsh</strong><br>Director</p>
  </div>
  <div class="footer">
    <div class="wordmark">Lumara</div>
    <div class="divider"></div>
    <div class="contact">
      <div class="sig">Owenmarsh</div>
      <div class="name">Owen Marsh</div>
      <div class="role">Director</div>
      <div class="line"><svg class="icon" width="6" height="6" viewBox="0 0 10 10"><circle cx="5" cy="5" r="5" fill="#8dc63f"/></svg>+61 400 555 018</div>
      <div class="line"><svg class="icon" width="6" height="6" viewBox="0 0 10 10"><circle cx="5" cy="5" r="5" fill="#8dc63f"/></svg>owen@lumara.com.au</div>
      <div class="line"><svg class="icon" width="6" height="6" viewBox="0 0 10 10"><circle cx="5" cy="5" r="5" fill="#8dc63f"/></svg>lumara.com.au</div>
    </div>
  </div>
  <svg class="corner" width="80" height="90" viewBox="0 0 80 90"><path d="M80 0 Q20 10 0 90 L80 90 Z" fill="#8dc63f"/></svg>
</section>

<section class="sheet card card-front" aria-label="Business card front">
  <div class="wordmark">Lumara</div>
  <div class="contact">
    <div class="name">Owen Marsh</div>
    <div class="role">Director</div>
    <div class="line"><svg class="icon" width="6" height="6" viewBox="0 0 10 10"><circle cx="5" cy="5" r="5" fill="#8dc63f"/></svg>+61 400 555 018</div>
    <div class="line"><svg class="icon" width="6" height="6" viewBox="0 0 10 10"><circle cx="5" cy="5" r="5" fill="#8dc63f"/></svg>owen@lumara.com.au</div>
    <div class="line"><svg class="icon" width="6" height="6" viewBox="0 0 10 10"><circle cx="5" cy="5" r="5" fill="#8dc63f"/></svg>lumara.com.au</div>
  </div>
</section>

<section class="sheet card card-back" aria-label="Business card back">
  <div class="wordmark light">Lumara</div>
  <div class="web"><svg class="icon" width="6" height="6" viewBox="0 0 10 10"><circle cx="5" cy="5" r="5" fill="#8dc63f"/></svg>lumara.com.au</div>
</section>

<section class="sheet envelope env-photo" aria-label="Envelope with director portrait">
  <div class="left contact">
    <div class="portrait" role="img" aria-label="Portrait photo of the director"></div>
    <div class="name">Owen Marsh</div>
    <div class="role">Director</div>
  </div>
  <div class="divider"></div>
  <div class="right contact">
    <div class="sig">Owenmarsh</div>
    <div class="rule-under"></div>
    <div class="wordmark mark-small">Lumara</div>
    <div class="line"><svg class="icon" width="9" height="9" viewBox="0 0 10 10"><circle cx="5" cy="5" r="5" fill="#8dc63f"/><path d="M3 2.5h1.3l.6 1.5-.8.6a4 4 0 0 0 1.6 1.6l.6-.8 1.5.6V7.5A1 1 0 0 1 6.8 8 5 5 0 0 1 2 3.2a1 1 0 0 1 1-.7z" fill="#fff"/></svg>+61 400 555 018</div>
    <div class="line"><svg class="icon" width="9" height="9" viewBox="0 0 10 10"><circle cx="5" cy="5" r="5" fill="#8dc63f"/><circle cx="5" cy="5" r="2.6" fill="none" stroke="#fff" stroke-width=".8"/></svg>lumara.com.au</div>
  </div>
</section>

<section class="sheet envelope env-plain" aria-label="Envelope">
  <div class="left">
    <div class="wordmark big">Lumara</div>
  </div>
  <div class="divider"></div>
  <div class="right contact">
    <div class="sig">Owenmarsh</div>
    <div class="rule-under"></div>
    <div class="name">Owen Marsh</div>
    <div class="role">Director</div>
    <div class="line"><svg class="icon" width="9" height="9" viewBox="0 0 10 10"><circle cx="5" cy="5" r="5" fill="#8dc63f"/><path d="M3 2.5h1.3l.6 1.5-.8.6a4 4 0 0 0 1.6 1.6l.6-.8 1.5.6V7.5A1 1 0 0 1 6.8 8 5 5 0 0 1 2 3.2a1 1 0 0 1 1-.7z" fill="#fff"/></svg>+61 400 555 018</div>
    <div class="line"><svg class="icon" width="9" height="9" viewBox="0 0 10 10"><circle cx="5" cy="5" r="5" fill="#8dc63f"/><circle cx="5" cy="5" r="2.6" fill="none" stroke="#fff" stroke-width=".8"/></svg>lumara.com.au</div>
  </div>
</section>

<section class="sheet poster" aria-label="Poster banner">
  <div class="wordmark">Lumara</div>
</section>

<section class="sheet box-lid" aria-label="Gift box lid">
  <div class="wordmark">Lumara</div>
</section>

</body>
</html>
```